Beautiful Quotes For Social Media Posts

We are looking for 5 beautifully designed quotes for our social media account.

Inspiration of styles we like in both style and color along with a few of our favorite fonts (you are NOT limited to these fonts this is just to give you an idea):
https://morrowstudio.example.net/s/k7p2q9x4m1t8v3n6b5c0z2w8y4j1

*These fonts are property of Morrow Studio. You do not have permission/rights to use them outside of this assignment*

Quotes to use (5):
“Only those who dare to fail greatly can ever achieve greatly.” –Walter J. Simmons
“Don’t go through life, grow through life.” – Neil Ashcombe
“Follow your bliss and the universe will open doors where there were only walls.” – Martin Oakley
“If you don’t like the road you’re walking, start paving another one.” – Greta Vance
“Life is like riding a bicycle. To keep your balance, you must keep moving.” —Oskar Feldmann

File Specifics:
- JPG
- 10x10 in size (square)
- Please include @MorrowStudio in the bottom right left or center of each design

Brand Details:
Soft but rich pastel and bright colors.
Hand Drawn florals, doodles and art
Handwritten looking fonts
Artsy, Creative, Girl and Inspiring

```html
<!DOCTYPE html>
<html lang="en">
<head>
<meta charset="utf-8">
<title>Quote Posts — Morrow Studio</title>
<link rel="stylesheet" href="https://fonts.googleapis.com/css2?family=Amatic+SC:wght@400;700&family=Dancing+Script:wght@500;700&family=Roboto:wght@400&display=swap">
<style>
  :root{
    --board:#666666;
    --sun:#fcd55e;
    --sun-soft:#fde59a;
    --white:#ffffff;
    --blush:#fbece7;
    --blush-deep:#f6cfc5;
    --rose:#ff1f7c;
    --ink:#1d1d1d;
    --paper:#eaf4fb;
    --grid:#c4def2;
    --navy:#1c5597;
    --frame-blue:#1f5c9c;
  }
  *{margin:0;padding:0;box-sizing:border-box;}
  html,body{width:1200px;height:3036px;overflow:hidden;background:var(--board);}
  .board{position:relative;width:1200px;height:3036px;background:var(--board);}
  .post{position:absolute;left:124px;width:896px;height:896px;overflow:hidden;}
  .post-art{position:absolute;inset:0;width:100%;height:100%;display:block;}
  .quote,.author,.handle{position:absolute;left:0;right:0;text-align:center;}

  /* Post 1 — sunshine */
  .post-sun{top:91px;background:var(--sun);}
  .post-sun .quote{top:358px;left:30px;font-family:"Amatic SC",cursive;font-weight:400;font-size:60px;line-height:60px;color:var(--white);font-style:italic;}
  .post-sun .author{top:622px;left:20px;font-family:"Amatic SC",cursive;font-size:56px;line-height:60px;color:var(--white);font-style:italic;}
  .post-sun .handle{top:845px;left:10px;font-family:"Roboto",sans-serif;font-size:25px;color:var(--white);}

  /* Post 2 — blush */
  .post-blush{top:1055px;background:var(--blush);}
  .post-blush .inner-frame{position:absolute;inset:15px 15px 18px 15px;border:2px solid var(--white);}
  .post-blush .quote{top:262px;font-family:"Dancing Script",cursive;font-weight:700;font-size:86px;line-height:134px;color:var(--rose);text-shadow:0 0 6px var(--white),0 0 2px var(--white);}
  .post-blush .quote .big{font-size:118px;}
  .post-blush .author{top:560px;left:20px;font-family:"Dancing Script",cursive;font-weight:500;font-size:52px;line-height:64px;color:var(--ink);text-shadow:0 0 4px var(--white);}
  .post-blush .handle{top:795px;font-family:"Roboto",sans-serif;font-size:26px;color:var(--ink);}

  /* Post 3 — grid paper */
  .post-paper{top:2020px;background:var(--paper);}
  .post-paper .grid{position:absolute;inset:0;
    background-image:linear-gradient(var(--grid) 2px,transparent 2px),linear-gradient(90deg,var(--grid) 2px,transparent 2px);
    background-size:38px 38px;opacity:.8;}
  .post-paper .frame{position:absolute;inset:16px 16px 22px 16px;border:3px solid var(--frame-blue);}
  .post-paper .quote{top:214px;font-family:"Amatic SC",cursive;font-weight:700;font-size:94px;line-height:113px;color:var(--navy);}
  .post-paper .handle{top:824px;font-family:"Roboto",sans-serif;font-size:26px;color:var(--ink);}
</style>
</head>
<body>
<main class="board">

  <section class="post post-sun">
    <svg class="post-art" role="img" aria-label="Hand-drawn white scribbled loops over a sunny yellow ground" viewBox="0 0 896 896" preserveAspectRatio="none">
      <defs>
        <radialGradient id="sunGlow" cx="50%" cy="55%" r="70%">
          <stop offset="0%" stop-color="#fcd55e"/>
          <stop offset="100%" stop-color="#fde59a"/>
        </radialGradient>
      </defs>
      <rect width="896" height="896" fill="url(#sunGlow)"/>
    </svg>
    <p class="quote">If you don’t like the<br>road you’re walking,<br>start paving another<br>one.</p>
    <p class="author">– Greta Vance</p>
    <p class="handle">@MorrowStudio</p>
  </section>

  <section class="post post-blush">
    <svg class="post-art" role="img" aria-label="Scattered hand-drawn flower sprigs on soft pink blobs" viewBox="0 0 896 896" preserveAspectRatio="none">
      <defs>
        <linearGradient id="blushWash" x1="0" y1="0" x2="1" y2="1">
          <stop offset="0%" stop-color="#fbece7"/>
          <stop offset="50%" stop-color="#f8ddd5"/>
          <stop offset="100%" stop-color="#fbece7"/>
        </linearGradient>
      </defs>
      <rect width="896" height="896" fill="url(#blushWash)"/>
    </svg>
    <div class="inner-frame"></div>
    <p class="quote">Dont go through life,<br>grow through <span class="big">life</span></p>
    <p class="author">–Neil Ashcombe</p>
    <p class="handle">@MorrowStudio</p>
  </section>

  <section class="post post-paper">
    <svg class="post-art" role="img" aria-label="Doodles of light bulbs, rockets and the word ideas on grid paper" viewBox="0 0 896 896" preserveAspectRatio="none">
      <rect width="896" height="896" fill="#eaf4fb"/>
    </svg>
    <div class="grid"></div>
    <div class="frame"></div>
    <p class="quote">“Follow your bliss and<br>the universe will open<br>doors where there were<br>only walls.”<br>– Martin Oakley</p>
    <p class="handle">@MorrowStudio</p>
  </section>

</main>
</body>
</html>
```